Business Card Design

We are a trucking company that do a lot of business one on one with shippers. Our enthusiasm, honesty and hard work make us a great company to work with. We want to not only leave a lasting impression by the professionalism of our drivers but also give them something to remember us by for the future. I have a logo already designed that matches the same logo on the trucks. Its simple yet captures people to remember the name. We are expanding our coverage area by almost 700 miles and want to get our brand out there by having shippers call us to come back and conduct more business. I would like part of the logo itself raised but the shadowing not to give it a unique look and feel.
Industry/Entity Type
Trucking Company
Contact Information for Business Card
K&M Hauling LLC
Kurt & Melissa Haverford
308.555.0142 Kurt
308.555.0187 Melissa
kmhaulingllc@examplemail.net
Look and feel

```html
<!DOCTYPE html>
<html lang="en">
<head>
<meta charset="utf-8">
<title>K&amp;M Hauling LLC – Business Card</title>
<link href="https://fonts.googleapis.com/css2?family=Open+Sans:wght@400;600;700&display=swap" rel="stylesheet">
<style>
  :root {
    --backdrop: #2b2b2b;
    --card: #ffffff;
    --ink: #111111;
    --muted: #333333;
    --tagline: #6a6a6a;
    --rule: #555555;
    --band: #0a0a0a;
  }
  html, body {
    margin: 0;
    padding: 0;
    width: 1200px;
    height: 750px;
    overflow: hidden;
    background: var(--backdrop);
    font-family: "Open Sans", Arial, sans-serif;
  }
  .card {
    position: absolute;
    left: 120px;
    top: 95px;
    width: 960px;
    height: 560px;
    background: var(--card);
    border-radius: 28px;
    overflow: hidden;
  }
  .card-band {
    position: absolute;
    left: 0;
    top: 440px;
    width: 960px;
    height: 62px;
    background: var(--band);
  }
  .brand {
    position: absolute;
    left: 60px;
    top: 150px;
    color: var(--ink);
  }
  .brand-initials {
    font-size: 124px;
    font-weight: 700;
    line-height: 1;
    letter-spacing: 2px;
  }
  .brand-name {
    font-size: 31px;
    font-weight: 600;
    color: var(--tagline);
    line-height: 1.2;
    margin-top: 4px;
    padding-left: 8px;
  }
  .divider {
    position: absolute;
    left: 462px;
    top: 90px;
    width: 1.5px;
    height: 320px;
    background: var(--rule);
  }
  .contacts {
    position: absolute;
    right: 70px;
    top: 148px;
    text-align: right;
    color: var(--ink);
  }
  .contact-name {
    font-size: 29px;
    font-weight: 600;
    margin: 0;
    line-height: 1.2;
  }
  .contact-line {
    display: flex;
    justify-content: flex-end;
    align-items: center;
    gap: 20px;
    font-size: 22px;
    color: var(--muted);
    margin: 10px 0 0;
  }
  .contact-line svg { width: 22px; height: 22px; flex: none; }
  .contact-block + .contact-block { margin-top: 38px; }
  .contact-email { margin-top: 34px; }
</style>
</head>
<body>
  <div class="card">
    <div class="card-band"></div>

    <div class="brand">
      <div class="brand-initials">K &amp; M</div>
      <div class="brand-name">Hauling LLC Ridgefield</div>
    </div>

    <div class="divider"></div>

    <div class="contacts">
      <div class="contact-block">
        <p class="contact-name">Melissa Haverford</p>
        <p class="contact-line">
          <svg viewBox="0 0 24 24"><rect x="1" y="1" width="22" height="22" rx="4" fill="var(--ink)"/><path fill="#fff" d="M8.2 5.5l2 2.6-1.3 1.6c.9 2 2.4 3.5 4.4 4.4l1.6-1.3 2.6 2-1.2 2.4c-5.2-.4-9.4-4.6-9.8-9.8z"/></svg>
          <span>308.555.0187</span>
        </p>
      </div>
      <div class="contact-block">
        <p class="contact-name">CO Kurt</p>
        <p class="contact-line">
          <svg viewBox="0 0 24 24"><rect x="1" y="1" width="22" height="22" rx="4" fill="var(--ink)"/><path fill="#fff" d="M8.2 5.5l2 2.6-1.3 1.6c.9 2 2.4 3.5 4.4 4.4l1.6-1.3 2.6 2-1.2 2.4c-5.2-.4-9.4-4.6-9.8-9.8z"/></svg>
          <span>308.555.0142</span>
        </p>
      </div>
      <p class="contact-line contact-email">
        <svg viewBox="0 0 24 24"><rect x="2" y="5" width="20" height="14" rx="2" fill="none" stroke="var(--ink)" stroke-width="2.4"/><path d="M3 6.5l9 6.5 9-6.5" fill="none" stroke="var(--ink)" stroke-width="2"/></svg>
        <span>kmhaulingllc@examplemail.net</span>
      </p>
    </div>
  </div>
</body>
</html>
```